BrightMeadow Vibrant Brochure Design

BrightMeadow is a renewable energy company based on the gold coast. we require a brochure that is vibrant and will catch our target audiences Eye. the format we would like is a landscape style 3 column folding brochure. the brochure should incorporate the colors from our logo. however.. this should not be a limiting factor as long as the colors are engaging, vibrant and attractive. please provide templates for headings and inserting text. the front page will have our logo on a vibrant natural background, bullet points of our products and space for a QR code that customers can scan, and room for our contact details down the bottom. the inside columns i would like to see a very simple design maybe our logo as a watermark backdrop with a vibrant banner down the bottom that will accommodate our statutory declarations. the three inside columns i would like a bordered text box for each column with formatting where i can offer three different products and there benefits in bullet form. the last two columns (the back of the brochure) will have again our logo as watermarked background and this will be our about us section.

please see attached photos and for brochure layout and logo design

Target Market(s)

adults between 25-45 and pensioners and elderly

Industry/Entity Type

Landscape

Requirements
Must have
• our company logo is a must.
Nice to have
• will be happy to view different styles and formats (does not have to be landscape 3 column format)
Should not have
• must not contain photos or pictures of solar panels or other electricity products. in fact keep pictures and artwork to a minimum

```html
<!DOCTYPE html>
<html lang="en">
<head>
<meta charset="utf-8">
<title>BrightMeadow Brochure – Inside Spread</title>
<link href="https://fonts.googleapis.com/css2?family=Archivo+Narrow:wght@700&family=Arimo:wght@400&display=swap" rel="stylesheet">
<style>
  :root {
    --paper: #ffffff;
    --ink: #111111;
    --frame-orange: #f5a623;
    --wash-orange: #fbe3b8;
    --wash-blue: #c9cde6;
    --wash-green: #cfe6c4;
    --wash-grey: #e4e4e4;
  }
  * { margin: 0; padding: 0; box-sizing: border-box; }
  html, body { width: 1200px; height: 927px; overflow: hidden; background: var(--paper); }
  .spread {
    position: relative;
    width: 1200px;
    height: 927px;
    background: var(--paper);
    color: var(--ink);
  }
  .watermark {
    position: absolute;
    inset: 0;
    width: 1200px;
    height: 927px;
  }
  .panel {
    position: absolute;
    top: 26px;
    width: 358px;
  }
  .panel--one { left: 24px; }
  .panel--two { left: 421px; }
  .panel--three { left: 818px; }
  .panel-heading {
    height: 87px;
    border: 4px solid var(--frame-orange);
    background: rgba(255,255,255,0.85);
    display: flex;
    align-items: center;
    justify-content: center;
    font-family: "Archivo Narrow", "Arial Narrow", sans-serif;
    font-weight: 700;
    font-size: 31px;
    letter-spacing: 0.5px;
  }
  .benefit {
    position: absolute;
    left: 4px;
    width: 356px;
  }
  .benefit-title {
    font-family: "Archivo Narrow", "Arial Narrow", sans-serif;
    font-weight: 700;
    font-size: 22px;
    line-height: 24px;
    margin-bottom: 2px;
  }
  .benefit-title::before { content: "\2022\00a0"; }
  .benefit-text {
    font-family: "Arimo", Arial, sans-serif;
    font-size: 12.6px;
    line-height: 18.2px;
  }
  .benefit--1 { top: 118px; }
  .benefit--2 { top: 278px; }
  .benefit--3 { top: 437px; }
  .benefit--4 { top: 598px; }
  .benefit--5 { top: 740px; }
</style>
</head>
<body>
<main class="spread">
  <svg class="watermark" viewBox="0 0 1200 927" role="img" aria-label="Faint BrightMeadow logo watermark in orange, blue, green and grey tones">
    <defs>
      <radialGradient id="wash-orange" cx="50%" cy="50%" r="50%">
        <stop offset="0%" stop-color="var(--wash-orange)" stop-opacity="0.9"/>
        <stop offset="100%" stop-color="var(--wash-orange)" stop-opacity="0"/>
      </radialGradient>
      <radialGradient id="wash-blue" cx="50%" cy="50%" r="50%">
        <stop offset="0%" stop-color="var(--wash-blue)" stop-opacity="0.9"/>
        <stop offset="100%" stop-color="var(--wash-blue)" stop-opacity="0"/>
      </radialGradient>
      <radialGradient id="wash-green" cx="50%" cy="50%" r="50%">
        <stop offset="0%" stop-color="var(--wash-green)" stop-opacity="0.9"/>
        <stop offset="100%" stop-color="var(--wash-green)" stop-opacity="0"/>
      </radialGradient>
      <radialGradient id="wash-grey" cx="50%" cy="50%" r="50%">
        <stop offset="0%" stop-color="var(--wash-grey)" stop-opacity="0.7"/>
        <stop offset="100%" stop-color="var(--wash-grey)" stop-opacity="0"/>
      </radialGradient>
    </defs>
    <rect x="300" y="0" width="600" height="560" fill="url(#wash-orange)"/>
    <rect x="0" y="440" width="560" height="487" fill="url(#wash-blue)"/>
    <rect x="640" y="440" width="560" height="487" fill="url(#wash-green)"/>
    <rect x="200" y="100" width="800" height="800" fill="url(#wash-grey)"/>
  </svg>

  <section class="panel panel--one">
    <h2 class="panel-heading">HEADING 1</h2>
    <article class="benefit benefit--1"><h3 class="benefit-title">Lorem ipsum Dolor</h3><p class="benefit-text">Duis facilisis justo eget nisl lacinia eget congue eros<br>consectetur. Duis semper, ligula sit amet fermentum<br>rutrum, diam ante lobortis nisi, ut auctor neque turpis eu<br>quam. Nam fringilla rutrum dolor, in venenatis est<br>pharetra sed. Donec id neque dui, sed ornare erat.<br>Nunc et pellentesque lectus.</p></article>
    <article class="benefit benefit--2"><h3 class="benefit-title">Sit Amet Consect</h3><p class="benefit-text">Duis facilisis justo eget nisl lacinia eget congue eros<br>consectetur. Duis semper, ligula sit amet fermentum<br>rutrum, diam ante lobortis nisi, ut auctor neque turpis eu<br>quam. Nam fringilla rutrum dolor, in venenatis est<br>pharetra sed. Donec id neque dui, sed ornare erat.<br>Nunc et pellentesque lectus.</p></article>
    <article class="benefit benefit--3"><h3 class="benefit-title">Etur Adipiscing</h3><p class="benefit-text">Duis facilisis justo eget nisl lacinia eget congue eros<br>consectetur. Duis semper, ligula sit amet fermentum<br>rutrum, diam ante lobortis nisi, ut auctor neque turpis eu<br>quam. Nam fringilla rutrum dolor, in venenatis est<br>pharetra sed. Donec id neque dui, sed ornare erat.<br>Nunc et pellentesque lectus.</p></article>
    <article class="benefit benefit--4"><h3 class="benefit-title">Elit Proin Auctor</h3><p class="benefit-text">Duis facilisis justo eget nisl lacinia eget congue eros<br>consectetur. Duis semper, ligula sit amet fermentum<br>rutrum, diam ante lobortis nisi, ut auctor neque turpis eu<br>quam. Nam fringilla rutrum dolor, in venenatis est<br>pharetra sed. Donec id neque dui, sed ornare erat.<br>Nunc et pellentesque lectus.</p></article>
    <article class="benefit benefit--5"><h3 class="benefit-title">Purus Id Metus</h3><p class="benefit-text">Duis facilisis justo eget nisl lacinia eget congue eros<br>consectetur. Duis semper, ligula sit amet fermentum<br>rutrum, diam ante lobortis nisi, ut auctor neque turpis eu<br>quam. Nam fringilla rutrum dolor, in venenatis est<br>pharetra sed. Donec id neque dui, sed ornare erat.<br>Nunc et pellentesque lectus.</p></article>
  </section>

  <section class="panel panel--two">
    <h2 class="panel-heading">HEADING 2</h2>
    <article class="benefit benefit--1"><h3 class="benefit-title">Lorem ipsum Dolor</h3><p class="benefit-text">Duis facilisis justo eget nisl lacinia eget congue eros<br>consectetur. Duis semper, ligula sit amet fermentum<br>rutrum, diam ante lobortis nisi, ut auctor neque turpis eu<br>quam. Nam fringilla rutrum dolor, in venenatis est<br>pharetra sed. Donec id neque dui, sed ornare erat.<br>Nunc et pellentesque lectus.</p></article>
    <article class="benefit benefit--2"><h3 class="benefit-title">Sit Amet Consect</h3><p class="benefit-text">Duis facilisis justo eget nisl lacinia eget congue eros<br>consectetur. Duis semper, ligula sit amet fermentum<br>rutrum, diam ante lobortis nisi, ut auctor neque turpis eu<br>quam. Nam fringilla rutrum dolor, in venenatis est<br>pharetra sed. Donec id neque dui, sed ornare erat.<br>Nunc et pellentesque lectus.</p></article>
    <article class="benefit benefit--3"><h3 class="benefit-title">Etur Adipiscing</h3><p class="benefit-text">Duis facilisis justo eget nisl lacinia eget congue eros<br>consectetur. Duis semper, ligula sit amet fermentum<br>rutrum, diam ante lobortis nisi, ut auctor neque turpis eu<br>quam. Nam fringilla rutrum dolor, in venenatis est<br>pharetra sed. Donec id neque dui, sed ornare erat.<br>Nunc et pellentesque lectus.</p></article>
    <article class="benefit benefit--4"><h3 class="benefit-title">Elit Proin Auctor</h3><p class="benefit-text">Duis facilisis justo eget nisl lacinia eget congue eros<br>consectetur. Duis semper, ligula sit amet fermentum<br>rutrum, diam ante lobortis nisi, ut auctor neque turpis eu<br>quam. Nam fringilla rutrum dolor, in venenatis est<br>pharetra sed. Donec id neque dui, sed ornare erat.<br>Nunc et pellentesque lectus.</p></article>
    <article class="benefit benefit--5"><h3 class="benefit-title">Purus Id Metus</h3><p class="benefit-text">Duis facilisis justo eget nisl lacinia eget congue eros<br>consectetur. Duis semper, ligula sit amet fermentum<br>rutrum, diam ante lobortis nisi, ut auctor neque turpis eu<br>quam. Nam fringilla rutrum dolor, in venenatis est<br>pharetra sed. Donec id neque dui, sed ornare erat.<br>Nunc et pellentesque lectus.</p></article>
  </section>

  <section class="panel panel--three">
    <h2 class="panel-heading">HEADING 3</h2>
    <article class="benefit benefit--1"><h3 class="benefit-title">Lorem ipsum Dolor</h3><p class="benefit-text">Duis facilisis justo eget nisl lacinia eget congue eros<br>consectetur. Duis semper, ligula sit amet fermentum<br>rutrum, diam ante lobortis nisi, ut auctor neque turpis eu<br>quam. Nam fringilla rutrum dolor, in venenatis est<br>pharetra sed. Donec id neque dui, sed ornare erat.<br>Nunc et pellentesque lectus.</p></article>
    <article class="benefit benefit--2"><h3 class="benefit-title">Sit Amet Consect</h3><p class="benefit-text">Duis facilisis justo eget nisl lacinia eget congue eros<br>consectetur. Duis semper, ligula sit amet fermentum<br>rutrum, diam ante lobortis nisi, ut auctor neque turpis eu<br>quam. Nam fringilla rutrum dolor, in venenatis est<br>pharetra sed. Donec id neque dui, sed ornare erat.<br>Nunc et pellentesque lectus.</p></article>
    <article class="benefit benefit--3"><h3 class="benefit-title">Etur Adipiscing</h3><p class="benefit-text">Duis facilisis justo eget nisl lacinia eget congue eros<br>consectetur. Duis semper, ligula sit amet fermentum<br>rutrum, diam ante lobortis nisi, ut auctor neque turpis eu<br>quam. Nam fringilla rutrum dolor, in venenatis est<br>pharetra sed. Donec id neque dui, sed ornare erat.<br>Nunc et pellentesque lectus.</p></article>
    <article class="benefit benefit--4"><h3 class="benefit-title">Elit Proin Auctor</h3><p class="benefit-text">Duis facilisis justo eget nisl lacinia eget congue eros<br>consectetur. Duis semper, ligula sit amet fermentum<br>rutrum, diam ante lobortis nisi, ut auctor neque turpis eu<br>quam. Nam fringilla rutrum dolor, in venenatis est<br>pharetra sed. Donec id neque dui, sed ornare erat.<br>Nunc et pellentesque lectus.</p></article>
    <article class="benefit benefit--5"><h3 class="benefit-title">Purus Id Metus</h3><p class="benefit-text">Duis facilisis justo eget nisl lacinia eget congue eros<br>consectetur. Duis semper, ligula sit amet fermentum<br>rutrum, diam ante lobortis nisi, ut auctor neque turpis eu<br>quam. Nam fringilla rutrum dolor, in venenatis est<br>pharetra sed. Donec id neque dui, sed ornare erat.<br>Nunc et pellentesque lectus.</p></article>
  </section>
</main>
</body>
</html>
```